New letter head for Air Conditioning business

We need a new professional letter head design to suit our new re-branded air conditioning business. Our new logo is attached

```html
<!DOCTYPE html>
<html lang="en">
<head>
<meta charset="utf-8">
<title>Coolvane Letterhead</title>
<link href="https://fonts.googleapis.com/css2?family=Exo+2:wght@500;600&display=swap" rel="stylesheet">
<style>
  :root {
    --ink: #3f3f41;
    --green: #66c288;
    --coral: #f26f63;
    --paper: #ffffff;
  }
  html, body {
    margin: 0;
    padding: 0;
    width: 848px;
    height: 1200px;
    overflow: hidden;
    background: var(--paper);
  }
  .letterhead {
    position: relative;
    width: 848px;
    height: 1200px;
    background: var(--paper);
    font-family: "Exo 2", sans-serif;
    color: var(--ink);
  }
  .brand {
    position: absolute;
    left: 56px;
    top: 72px;
    display: flex;
    align-items: center;
    gap: 16px;
  }
  .brand-dot {
    width: 38px;
    height: 38px;
    border-radius: 50%;
    background: var(--green);
  }
  .brand-name {
    font-family: "Exo 2", sans-serif;
    font-weight: 600;
    font-size: 38px;
    letter-spacing: 4px;
    color: var(--ink);
    line-height: 1;
  }
  .contact {
    position: absolute;
    left: 583px;
    top: 56px;
    margin: 0;
    padding: 0;
    list-style: none;
  }
  .contact-item {
    display: flex;
    align-items: flex-start;
    gap: 15px;
    margin-bottom: 8px;
  }
  .contact-icon {
    width: 20px;
    height: 20px;
    flex: none;
  }
  .contact-text {
    font-size: 12.5px;
    font-weight: 500;
    line-height: 14px;
    padding-top: 2px;
    color: var(--ink);
  }
  .footer-wave {
    position: absolute;
    left: 0;
    top: 0;
    width: 848px;
    height: 1200px;
    pointer-events: none;
  }
</style>
</head>
<body>
<div class="letterhead">
  <div class="brand">
    <span class="brand-dot"></span>
    <span class="brand-name">COOLVANE</span>
  </div>

  <ul class="contact">
    <li class="contact-item">
      <svg class="contact-icon" viewBox="0 0 20 20" aria-hidden="true">
        <rect width="20" height="20" rx="5" fill="var(--coral)"/>
        <path d="M10 4a4 4 0 0 0-4 4c0 3 4 8 4 8s4-5 4-8a4 4 0 0 0-4-4z" fill="#fff"/>
        <circle cx="10" cy="8" r="1.5" fill="var(--coral)"/>
      </svg>
      <span class="contact-text">Post Box: 418205, Dubai, UAE</span>
    </li>
    <li class="contact-item">
      <svg class="contact-icon" viewBox="0 0 20 20" aria-hidden="true">
        <rect width="20" height="20" rx="5" fill="var(--coral)"/>
        <path d="M4 8c0-2 12-2 12 0v1h-3V8H7v1H4z" fill="#fff"/>
        <path d="M6 10h8l1 5H5z" fill="#fff"/>
        <circle cx="10" cy="12.5" r="1.3" fill="var(--coral)"/>
      </svg>
      <span class="contact-text">+0000 0000000<br>+0000 0000000</span>
    </li>
    <li class="contact-item">
      <svg class="contact-icon" viewBox="0 0 20 20" aria-hidden="true">
        <rect width="20" height="20" rx="5" fill="var(--coral)"/>
        <rect x="4.5" y="6" width="11" height="8" rx="1" fill="#fff"/>
        <path d="M4.8 6.5 10 10.5l5.2-4" fill="none" stroke="var(--coral)" stroke-width="1.2"/>
      </svg>
      <span class="contact-text">info@coolvane air condition</span>
    </li>
  </ul>

  <svg class="footer-wave" viewBox="0 0 848 1200" aria-hidden="true">
    <path d="M280 1200 Q700 1190 848 1093 L848 1200 Z" fill="var(--green)"/>
    <path d="M0 1152 Q424 1240 848 1150 L848 1200 L0 1200 Z" fill="var(--ink)"/>
  </svg>
</div>
</body>
</html>
```